Barbecue Wine Vintage or Retro lable design

We need a label design for a barbecue / barbeque wine in a unit of 5 liters. It is a project between Halvard Kabinett - a wine trade company with rare wines - and a specialized winery in Austria named Winery Brunnacher. The wines are in a highest quality level. The design should be in a vintage or retro style. The bottle is attached. The size of the lable must be 17 inches and the height is 13 inches or inches in width 6,69291 and height 5,11811. We have two wines so we need the same design two times. One with the wine name "Lord Crimson No. 5" and the other "Lord Pale No. 5" and both with the same design. Or the possibility to change our name in the design / file. (eg we have indesign cs6, photoshop cs6 or adobe illustrater) At the front side must stay halvardkabinett.at and winery Brunnacher.

Target Market(s)

Grill and Barbeque Party Lovers, Wine Lovers, Hipster Foodies, Natural Wine Lovers, Shoppers Barbeque Store

Colors

Designer to choose colors to be used in the design.

Requirements
Must have
• It needs to be simple, clean. Vintage or Retro Style. The aim is to create a label design for the bottle.
Nice to have
• Vintage or retro pictures are possible or self made draws

```html
<!DOCTYPE html>
<html lang="en">
<head>
<meta charset="utf-8">
<title>Barbecue Wine Label – Colour Variants</title>
<link rel="stylesheet" href="https://fonts.googleapis.com/css2?family=IM+Fell+English&family=Source+Sans+3:wght@400;600&display=swap">
<style>
  :root {
    --backdrop: #968177;
    --shadow: rgba(0,0,0,.45);
    --sage: #84986a;
    --navy: #221c33;
    --plum-frame: #5e2633;
    --wine: #5a0f1a;
    --wine-frame: #5a0e1a;
    --oxblood: #2c0c17;
    --paper: #ffffff;
    --ink-light: #ffffff;
    --ink-dark: #111111;
    --seal-red: #e31b23;
    --seal-deep: #4a1222;
    --ribbon-light: rgba(255,255,255,.14);
    --ribbon-dark: rgba(0,0,0,.08);
  }
  * { box-sizing: border-box; margin: 0; padding: 0; }
  html, body { width: 1200px; height: 1200px; overflow: hidden; }
  body { background: var(--backdrop); position: relative; font-family: "Source Sans 3", sans-serif; }

  .label {
    position: absolute; width: 502px; height: 386px;
    box-shadow: 8px 10px 12px var(--shadow);
  }
  .label--navy { left: 79px; top: 200px; background: var(--sage); }
  .label--wine { left: 620px; top: 200px; background: var(--plum-frame); }
  .label--paper { left: 79px; top: 613px; background: var(--backdrop); border: 1px solid #3a2e2a; box-shadow: none; }
  .label--oxblood { left: 620px; top: 613px; background: var(--wine-frame); }

  .label__panel {
    position: absolute; left: 18px; top: 12px; right: 13px; bottom: 13px;
    color: var(--ink-light);
  }
  .label--navy .label__panel { background: var(--navy); }
  .label--wine .label__panel { background: var(--wine); }
  .label--paper .label__panel { background: var(--paper); color: var(--ink-dark); box-shadow: 6px 8px 10px var(--shadow); left: 17px; top: 11px; right: 14px; bottom: 12px; }
  .label--oxblood .label__panel { background: var(--oxblood); }

  .banner {
    position: absolute; left: 129px; top: 22px; width: 210px; height: 40px;
    border-radius: 20px;
    background: var(--ribbon-light);
    display: flex; align-items: center; justify-content: center;
  }
  .label--paper .banner { background: var(--ribbon-dark); }
  .banner__title { font-family: "IM Fell English", serif; font-size: 18px; letter-spacing: .6px; }

  .copy {
    position: absolute; top: 105px; width: 185px;
    font-size: 13.6px; line-height: 17.4px;
  }
  .copy--left { left: 37px; }
  .copy--right { left: 247px; }
  .line { display: block; text-align: justify; text-align-last: justify; white-space: nowrap; }
  .line--end { text-align-last: left; }
  .credits { margin-top: 11px; font-weight: 600; }

  .maker {
    position: absolute; left: 247px; top: 262px; width: 183px; height: 72px;
    display: flex; align-items: center; justify-content: flex-end; gap: 10px;
  }
  .maker__name { font-size: 13.6px; font-weight: 600; }
  .maker__dot { width: 72px; height: 72px; border-radius: 50%; flex: none; }
  .maker__dot--red { background: var(--seal-red); }
  .maker__dot--white { background: var(--paper); }
  .maker__dot--deep { background: var(--seal-deep); }
</style>
</head>
<body>

<section class="label label--navy">
  <div class="label__panel">
    <div class="banner" role="img" aria-label="Vintage scroll ribbon ornament"><span class="banner__title">Red wine</span></div>
    <p class="copy copy--left">
      <span class="line">Lorem ipsum dolor sit amet,</span>
      <span class="line">consectetur adipiscing elit,</span>
      <span class="line">sed do eiusmod tempor inci-</span>
      <span class="line">didunt ut labore et dolore</span>
      <span class="line">magna aliqua. Ut enim ad</span>
      <span class="line">minim veniam, quis nostrud</span>
      <span class="line">exercitation ullamco laboris</span>
      <span class="line">nisi ut aliquip ex ea commodo</span>
      <span class="line">consequat. Duis aute irure</span>
      <span class="line">dolor in reprehenderit in</span>
      <span class="line">voluptate velit esse cillum</span>
      <span class="line">dolore eu fugiat nulla pariatur.</span>
      <span class="line">Excepteur sint occaecat cupi-</span>
    </p>
    <div class="copy copy--right">
      <p><span class="line">datat non proident, sunt in</span><span class="line">culpa qui officia deserunt</span><span class="line line--end">mollit anim id est laborum.</span></p>
      <p class="credits">Barbeque wine<br>halvardkabinett.at<br>Weingut Brunnacher</p>
    </div>
    <div class="maker"><span class="maker__name">Halvard Kabinett</span><span class="maker__dot maker__dot--red"></span></div>
  </div>
</section>

<section class="label label--wine">
  <div class="label__panel">
    <div class="banner" role="img" aria-label="Vintage scroll ribbon ornament"><span class="banner__title">Red wine</span></div>
    <p class="copy copy--left">
      <span class="line">Lorem ipsum dolor sit amet,</span>
      <span class="line">consectetur adipiscing elit,</span>
      <span class="line">sed do eiusmod tempor inci-</span>
      <span class="line">didunt ut labore et dolore</span>
      <span class="line">magna aliqua. Ut enim ad</span>
      <span class="line">minim veniam, quis nostrud</span>
      <span class="line">exercitation ullamco laboris</span>
      <span class="line">nisi ut aliquip ex ea commodo</span>
      <span class="line">consequat. Duis aute irure</span>
      <span class="line">dolor in reprehenderit in</span>
      <span class="line">voluptate velit esse cillum</span>
      <span class="line">dolore eu fugiat nulla pariatur.</span>
      <span class="line">Excepteur sint occaecat cupi-</span>
    </p>
    <div class="copy copy--right">
      <p><span class="line">datat non proident, sunt in</span><span class="line">culpa qui officia deserunt</span><span class="line line--end">mollit anim id est laborum.</span></p>
      <p class="credits">Barbeque wine<br>halvardkabinett.at<br>Weingut Brunnacher</p>
    </div>
    <div class="maker"><span class="maker__name">Halvard Kabinett</span><span class="maker__dot maker__dot--white"></span></div>
  </div>
</section>

<section class="label label--paper">
  <div class="label__panel">
    <div class="banner" role="img" aria-label="Vintage scroll ribbon ornament"><span class="banner__title">Red wine</span></div>
    <p class="copy copy--left">
      <span class="line">Lorem ipsum dolor sit amet,</span>
      <span class="line">consectetur adipiscing elit,</span>
      <span class="line">sed do eiusmod tempor inci-</span>
      <span class="line">didunt ut labore et dolore</span>
      <span class="line">magna aliqua. Ut enim ad</span>
      <span class="line">minim veniam, quis nostrud</span>
      <span class="line">exercitation ullamco laboris</span>
      <span class="line">nisi ut aliquip ex ea commo-</span>
      <span class="line">do consequat. Duis aute</span>
      <span class="line">irure dolor in reprehenderit</span>
      <span class="line">in voluptate velit esse cillum</span>
      <span class="line">dolore eu fugiat nulla paria-</span>
    </p>
    <div class="copy copy--right">
      <p><span class="line">tur. Excepteur sint occaecat</span><span class="line">cupidatat non proident,</span><span class="line">sunt in culpa qui officia dese-</span><span class="line">runt mollit anim id est labo-</span><span class="line line--end">rum.</span></p>
      <p class="credits">Barbeque wine<br>halvardkabinett.at<br>Weingut Brunnacher</p>
    </div>
    <div class="maker"><span class="maker__name">Halvard Kabinett</span><span class="maker__dot maker__dot--red"></span></div>
  </div>
</section>

<section class="label label--oxblood">
  <div class="label__panel">
    <div class="banner" role="img" aria-label="Vintage scroll ribbon ornament"><span class="banner__title">Red wine</span></div>
    <p class="copy copy--left">
      <span class="line">Lorem ipsum dolor sit amet,</span>
      <span class="line">consectetur adipiscing elit,</span>
      <span class="line">sed do eiusmod tempor inci-</span>
      <span class="line">didunt ut labore et dolore</span>
      <span class="line">magna aliqua. Ut enim ad</span>
      <span class="line">minim veniam, quis nostrud</span>
      <span class="line">exercitation ullamco laboris</span>
      <span class="line">nisi ut aliquip ex ea commodo</span>
      <span class="line">consequat. Duis aute irure</span>
      <span class="line">dolor in reprehenderit in</span>
      <span class="line">voluptate velit esse cillum</span>
      <span class="line">dolore eu fugiat nulla pariatur.</span>
      <span class="line">Excepteur sint occaecat cupi-</span>
    </p>
    <div class="copy copy--right">
      <p><span class="line">datat non proident, sunt in</span><span class="line">culpa qui officia deserunt</span><span class="line line--end">mollit anim id est laborum.</span></p>
      <p class="credits">Barbeque wine<br>halvardkabinett.at<br>Weingut Brunnacher</p>
    </div>
    <div class="maker"><span class="maker__name">Halvard Kabinett</span><span class="maker__dot maker__dot--deep"></span></div>
  </div>
</section>

</body>
</html>
```